Home Improvements Website

I would like a website that matches our business colour scheme and uses the fonts consistent without logo. (Monserrat, Chosence & Big Noddle Tiling).
We will need numerous sections: homepage, about us, services (with tiles or links to each service - building, landscaping, decking, maintenance, roofing, gutters etc) current projects (which must be easily editable by me, who is not too tech savvy) and a contacts page with enquiry form we can link to our job management service (Tradify).

```html
<!DOCTYPE html>
<html lang="en">
<head>
<meta charset="UTF-8">
<title>Contact Us – Kestrel Home Improvements</title>
<link href="https://fonts.googleapis.com/css2?family=Montserrat:wght@400;500;600&display=swap" rel="stylesheet">
<style>
  :root {
    --bar: #212529;
    --nav-text: #c8cacc;
    --heading: #212529;
    --label: #2a2f5e;
    --body: #2a2f5e;
    --field-border: #dee2e6;
    --accent: #008000;
    --white: #ffffff;
    --brand: #3a9a3a;
  }
  * { box-sizing: border-box; margin: 0; padding: 0; }
  html, body { width: 1200px; height: 741px; overflow: hidden; }
  body {
    position: relative;
    background: var(--white);
    font-family: "Montserrat", sans-serif;
    color: var(--body);
  }
  .site-header {
    position: absolute; left: 0; top: 0; width: 1200px; height: 66px;
    background: var(--bar);
  }
  .brand {
    position: absolute; left: 196px; top: 22px;
    display: flex; align-items: center; gap: 6px;
    color: var(--white); font-size: 11px; font-weight: 600;
  }
  .brand-dot { width: 14px; height: 14px; border-radius: 50%; background: var(--brand); }
  .main-nav {
    position: absolute; right: 200px; top: 26px;
    display: flex; gap: 10px; font-size: 10.6px;
  }
  .main-nav a { color: var(--nav-text); text-decoration: none; }
  .contact {
    position: absolute; left: 332.5px; top: 95px; width: 535px;
  }
  .contact-title {
    text-align: center; font-weight: 400; font-size: 27.5px;
    color: var(--heading); line-height: 34px; margin-bottom: 2px;
  }
  .field { margin-bottom: 10px; }
  .field label { display: block; font-size: 10px; color: var(--label); line-height: 13px; margin-bottom: 6px; }
  .field input, .field .select, .field textarea {
    display: block; width: 100%; height: 24px;
    border: 1px solid var(--field-border); border-radius: 4px;
    font-family: inherit; font-size: 10px; color: var(--heading);
    background: var(--white); padding: 0 8px; line-height: 22px;
  }
  .field textarea { height: 69px; resize: none; }
  .send-btn {
    display: inline-block; margin-top: 0; height: 24px; width: 89px;
    background: var(--accent); color: var(--white); border: none; border-radius: 4px;
    font-family: inherit; font-size: 10.4px;
  }
  .contact-info { margin-top: 29px; font-size: 10px; line-height: 15px; }
  .contact-info p { margin-bottom: 10px; }
  .contact-info strong { font-weight: 600; color: var(--heading); }
  .site-footer {
    position: absolute; left: 0; top: 696px; width: 1200px; height: 45px;
    background: var(--bar); color: var(--white);
    text-align: center; font-size: 10px; line-height: 34px;
  }
</style>
</head>
<body>
  <header class="site-header">
    <div class="brand"><span class="brand-dot"></span>Kestrel</div>
    <nav class="main-nav">
      <a href="#">Home</a><a href="#">About Us</a><a href="#">Services</a><a href="#">Current Projects</a><a href="#">Contact Us</a>
    </nav>
  </header>

  <main class="contact">
    <h1 class="contact-title">Contact Us</h1>
    <form class="enquiry-form">
      <div class="field"><label>Full Name</label><input type="text"></div>
      <div class="field"><label>Phone</label><input type="text"></div>
      <div class="field"><label>Email</label><input type="text"></div>
      <div class="field"><label>Job Type</label><div class="select">Landscaping</div></div>
      <div class="field"><label>Message</label><textarea></textarea></div>
      <button type="button" class="send-btn">Send Message</button>
    </form>
    <section class="contact-info">
      <p>If you have any questions or would like to discuss your next project, please get in touch with us. Our team is here to assist you with all your home improvement needs.</p>
      <p><strong>Email:</strong> info@kestrelhomeimprovements.com</p>
      <p><strong>Phone:</strong> MARCUS: 0412 555 218</p>
      <p><strong>Phone:</strong> HELEN: 0433 555 907</p>
      <p><strong>Address:</strong> 123 Home Improvement Lane, City, State, ZIP</p>
      <p>We look forward to hearing from you and helping you with your home improvement projects.</p>
    </section>
  </main>

  <footer class="site-footer">© 2024 Kestrel Home Improvements. All rights reserved.</footer>
</body>
</html>
```